OTU Consulting Firm needs artwork for foyer

We are looking for a piece of artwork for our foyer entrance. It will be displayed on the white wall above the two armchairs.

The piece could be meaningful to our organisation, but also could be of an abstract nature. We want the artwork to be striking/interesting as it is displayed in the foyer. The artwork would be printed on a landscape canvas print with dimensions 76 cm x 152 cm.

Please see attached word document "Velm Studio" for all specifications.

Target Market(s)

Industry/Entity Type

Consulting

Requirements
Must have
• Please see attached word document "Velm Studio" for all specifications.
Nice to have
Should not have

```html
<!DOCTYPE html>
<html lang="en">
<head>
<meta charset="UTF-8">
<title>OTU Consulting Firm — Foyer Values Artwork</title>
<link href="https://fonts.googleapis.com/css2?family=Montserrat:wght@700;800&display=swap" rel="stylesheet">
<style>
  :root {
    --page-bg: #ffffff;
    --panel-edge: #1b202b;
    --panel-blue: #0b78c0;
    --connector: #8fd3f2;
    --node-fill: #ffffff;
    --node-text: #0b5f9c;
  }
  html, body {
    margin: 0;
    padding: 0;
    width: 1200px;
    height: 900px;
    overflow: hidden;
    background: var(--page-bg);
  }
  .canvas {
    position: relative;
    width: 1200px;
    height: 900px;
  }
  .values-artwork {
    position: absolute;
    left: 60px;
    top: 177px;
    width: 1080px;
    height: 547px;
  }
  .panel-edge { fill: var(--panel-edge); }
  .panel-face { fill: var(--panel-blue); }
  .connector {
    stroke: var(--connector);
    stroke-width: 1.6;
    stroke-linecap: round;
    fill: none;
  }
  .node-box {
    fill: var(--node-fill);
    stroke: var(--connector);
    stroke-width: 0.5;
  }
  .node-label {
    fill: var(--node-text);
    font-family: "Montserrat", sans-serif;
    font-weight: 800;
    font-size: 3.1px;
    text-anchor: middle;
    letter-spacing: 0.05px;
  }
</style>
</head>
<body>
<main class="canvas">
  <svg class="values-artwork" viewBox="0 0 300 152" role="img" aria-label="OTU Consulting Firm values map">
    <rect class="panel-edge" x="0" y="0" width="300" height="152" rx="16"/>
    <rect class="panel-face" x="5" y="5" width="295" height="147" rx="14"/>

    <g class="connectors">
      <line class="connector" x1="34" y1="75" x2="70" y2="41"/>
      <line class="connector" x1="70" y1="41" x2="122" y2="27"/>
      <line class="connector" x1="122" y1="27" x2="173" y2="27"/>
      <line class="connector" x1="173" y1="27" x2="227" y2="41"/>
      <line class="connector" x1="227" y1="41" x2="262" y2="75"/>
      <line class="connector" x1="262" y1="75" x2="227" y2="109"/>
      <line class="connector" x1="227" y1="109" x2="173" y2="127"/>
      <line class="connector" x1="173" y1="127" x2="122" y2="127"/>
      <line class="connector" x1="122" y1="127" x2="70" y2="109"/>
      <line class="connector" x1="70" y1="109" x2="34" y2="75"/>
      <line class="connector" x1="34" y1="75" x2="262" y2="75"/>
    </g>

    <g class="node">
      <rect class="node-box" x="51" y="33" width="38" height="16" rx="2"/>
      <text class="node-label" x="70" y="40.2"><tspan x="70">POSITIVE AND</tspan><tspan x="70" dy="3.6">SUPPORTIVE</tspan></text>
    </g>
    <g class="node">
      <rect class="node-box" x="103" y="19" width="38" height="16" rx="2"/>
      <text class="node-label" x="122" y="26.2"><tspan x="122">QUALITY AND</tspan><tspan x="122" dy="3.6">EXCELLENCE</tspan></text>
    </g>
    <g class="node">
      <rect class="node-box" x="154" y="19" width="38" height="16" rx="2"/>
      <text class="node-label" x="173" y="26.2"><tspan x="173">DEVELOPMENT</tspan><tspan x="173" dy="3.6">AND GROWTH</tspan></text>
    </g>
    <g class="node">
      <rect class="node-box" x="208" y="33" width="38" height="16" rx="2"/>
      <text class="node-label" x="227" y="42.1">CLIENT FOCUS</text>
    </g>
    <g class="node">
      <rect class="node-box" x="15" y="67" width="38" height="16" rx="2"/>
      <text class="node-label" x="34" y="74.2"><tspan x="34">INTEGRITY AND</tspan><tspan x="34" dy="3.6">ACCOUNTABILITY</tspan></text>
    </g>
    <g class="node">
      <rect class="node-box" x="91" y="67" width="38" height="16" rx="2"/>
      <text class="node-label" x="110" y="76.1">COLLABORATION</text>
    </g>
    <g class="node">
      <rect class="node-box" x="168" y="67" width="38" height="16" rx="2"/>
      <text class="node-label" x="187" y="76.1">RESPONSIVE</text>
    </g>
    <g class="node">
      <rect class="node-box" x="243" y="67" width="38" height="16" rx="2"/>
      <text class="node-label" x="262" y="76.1">ADMINISTRATION</text>
    </g>
    <g class="node">
      <rect class="node-box" x="51" y="101" width="38" height="16" rx="2"/>
      <text class="node-label" x="70" y="110.1">NIMBLE</text>
    </g>
    <g class="node">
      <rect class="node-box" x="103" y="119" width="38" height="16" rx="2"/>
      <text class="node-label" x="122" y="128.1">INNOVATION</text>
    </g>
    <g class="node">
      <rect class="node-box" x="154" y="119" width="38" height="16" rx="2"/>
      <text class="node-label" x="173" y="128.1">EVALUATION</text>
    </g>
    <g class="node">
      <rect class="node-box" x="208" y="101" width="38" height="16" rx="2"/>
      <text class="node-label" x="227" y="110.1">CONSULTING</text>
    </g>
  </svg>
</main>
</body>
</html>
```